BOLD & MINIMALIST DESIGN NEEDED

We want a very bold but minimalistic business card design that is impactful and utilizes both sides of the business card. Our current logo is included for your use.

We want bold fonts and good use of negative space. We don't want the logo to overpower the design.

Target Market(s)

Professionals who are building new commercial buildings.

Industry/Entity Type

Construction

Contact Information for Business Card

Name, Title, email, office phone, cell phone, website

Font styles to use
Serif
Sans Serif

Requirements
Must have
• Bold design!

```html
<!DOCTYPE html>
<html lang="en">
<head>
<meta charset="utf-8">
<title>Ridgeline Build Co – Business Card</title>
<link rel="stylesheet" href="https://fonts.googleapis.com/css2?family=Montserrat:wght@700;800&display=swap">
<style>
  :root {
    --backdrop: #0c0c0c;
    --card: #ffffff;
    --ink: #0a0a0a;
    --accent: #86c126;
  }
  * { margin: 0; padding: 0; box-sizing: border-box; }
  html, body {
    width: 1200px; height: 1199px; overflow: hidden;
    background: var(--backdrop);
    font-family: "Montserrat", Arial, sans-serif;
    color: var(--ink);
  }
  .card {
    position: absolute; left: 207px; width: 790px; height: 453px;
    background: var(--card);
  }
  .card--front { top: 124px; }
  .card--back { top: 622px; }
  .card__band {
    position: absolute; left: 0; right: 0; bottom: 0; height: 25px;
    background: var(--accent);
  }
  .contact { position: absolute; left: 68px; top: 104px; list-style: none; }
  .contact__item {
    display: flex; align-items: flex-start; gap: 14px;
    font-size: 19px; font-weight: 700; height: 51px;
  }
  .contact__icon { width: 25px; height: 25px; flex: none; margin-top: -1px; }
  .contact__name { font-size: 25px; line-height: 1; margin-top: -1px; }
  .contact__title { display: block; font-size: 13px; margin-top: 3px; }
  .contact__item--name { height: 66px; }
  .wordmark {
    position: absolute; display: flex; align-items: center; gap: 12px;
    font-weight: 800; color: var(--ink); letter-spacing: 1px;
  }
  .wordmark__square { width: 22px; height: 22px; background: var(--accent); flex: none; }
  .wordmark--front { left: 500px; top: 168px; font-size: 30px; }
  .wordmark--back { left: 0; right: 0; top: 200px; justify-content: center; font-size: 46px; }
  .wordmark--back .wordmark__square { width: 32px; height: 32px; }
</style>
</head>
<body>
  <section class="card card--front">
    <ul class="contact">
      <li class="contact__item contact__item--name">
        <svg class="contact__icon" viewBox="0 0 24 24"><circle cx="12" cy="12" r="12" fill="#0a0a0a"/><circle cx="12" cy="9" r="3.6" fill="#fff"/><path d="M5.5 18.5c1-3.5 3.5-5 6.5-5s5.5 1.5 6.5 5z" fill="#fff"/></svg>
        <div><span class="contact__name">JORDAN REYES</span><span class="contact__title">Architect</span></div>
      </li>
      <li class="contact__item">
        <svg class="contact__icon" viewBox="0 0 24 24"><circle cx="12" cy="12" r="12" fill="#0a0a0a"/><path d="M8 6l2.2 2.6-1.2 1.6c.9 1.9 2.4 3.4 4.3 4.3l1.6-1.2L17.5 16l-1.3 2c-5.2-.4-9.4-4.6-9.8-9.8z" fill="#fff"/></svg>
        <span>321 654 987 012</span>
      </li>
      <li class="contact__item">
        <svg class="contact__icon" viewBox="0 0 24 24"><circle cx="12" cy="12" r="12" fill="#0a0a0a"/><rect x="6" y="8" width="12" height="8" fill="#fff"/><path d="M6 8l6 5 6-5" fill="none" stroke="#0a0a0a" stroke-width="1.2"/></svg>
        <span>hello@jordanreyes.com</span>
      </li>
      <li class="contact__item">
        <svg class="contact__icon" viewBox="0 0 24 24"><circle cx="12" cy="12" r="12" fill="#0a0a0a"/><g fill="none" stroke="#fff" stroke-width="1.3"><circle cx="12" cy="12" r="6"/><ellipse cx="12" cy="12" rx="2.6" ry="6"/><path d="M6 12h12M7 9h10M7 15h10"/></g></svg>
        <span>www.jordanreyes.com</span>
      </li>
      <li class="contact__item">
        <svg class="contact__icon" viewBox="0 0 24 24"><circle cx="12" cy="12" r="12" fill="#0a0a0a"/><path d="M12 5a4.5 4.5 0 0 0-4.5 4.5C7.5 13 12 19 12 19s4.5-6 4.5-9.5A4.5 4.5 0 0 0 12 5z" fill="#fff"/><circle cx="12" cy="9.5" r="1.7" fill="#0a0a0a"/></svg>
        <span>BROOKFIELD TOWER, OAK DISTRICT</span>
      </li>
    </ul>
    <div class="wordmark wordmark--front"><span class="wordmark__square"></span>RIDGELINE</div>
    <div class="card__band"></div>
  </section>

  <section class="card card--back">
    <div class="wordmark wordmark--back"><span class="wordmark__square"></span>RIDGELINE BUILD CO</div>
    <div class="card__band"></div>
  </section>
</body>
</html>
```